R&V Architects and Interiors Business Card

We need to redesign our business card. We had used white vellum wih grey logo and txt in the past. I would like to bring a little life into our cards without being over the top. I think I will be going away from the vellum and printing soft touch business cards.
I have attached what we currently have and our new logo design.

```html
<!DOCTYPE html>
<html lang="en">
<head>
<meta charset="utf-8">
<title>R&amp;V Architects and Interiors – Business Card</title>
<link href="https://fonts.googleapis.com/css2?family=Jost:wght@300;400;500;600&display=swap" rel="stylesheet">
<style>
  :root {
    --stage: #6f6f6f;
    --card-front: #bfbfbf;
    --card-back: #ffffff;
    --mark-light: #ffffff;
    --mark-faint: #d2d2d2;
    --mark-faint-text: #c6c6c6;
    --ink: #111111;
  }
  * { margin: 0; padding: 0; box-sizing: border-box; }
  html, body {
    width: 1200px; height: 1200px; overflow: hidden;
    background: var(--stage);
    font-family: "Jost", "Futura", sans-serif;
  }
  .canvas { position: relative; width: 1200px; height: 1200px; }
  .card {
    position: absolute; left: 228px; width: 746px; height: 435px; overflow: hidden;
  }
  .card--front { top: 156px; background: var(--card-front); }
  .card--back { top: 662px; background: var(--card-back); }

  /* Front */
  .front-square {
    position: absolute; left: 48px; top: 52px; width: 122px; height: 122px;
    background: var(--mark-light);
  }
  .front-name {
    position: absolute; right: 60px; bottom: 18px;
    color: var(--mark-light); font-weight: 400; font-size: 32px;
    letter-spacing: 4.2px; line-height: 1; white-space: nowrap;
  }
  .front-name-vertical {
    position: absolute; right: 12px; bottom: 56px;
    writing-mode: vertical-rl; transform: rotate(180deg);
    color: var(--mark-light); font-weight: 400; font-size: 32px;
    letter-spacing: 4.2px; line-height: 1; white-space: nowrap;
  }

  /* Back */
  .back-square {
    position: absolute; left: 111px; top: 139px; width: 166px; height: 166px;
    background: var(--mark-faint);
  }
  .back-name {
    position: absolute; left: 113px; top: 311px;
    color: var(--mark-faint-text); font-weight: 400; font-size: 15px;
    letter-spacing: 2.1px; line-height: 1; white-space: nowrap;
  }
  .back-name-vertical {
    position: absolute; left: 279px; top: 139px; height: 170px;
    writing-mode: vertical-rl; transform: rotate(180deg);
    color: var(--mark-faint-text); font-weight: 400; font-size: 15px;
    letter-spacing: 2.1px; line-height: 1; white-space: nowrap; text-align: left;
  }
  .contact {
    position: absolute; left: 331px; width: 400px; text-align: center; color: var(--ink);
  }
  .contact-name { top: 115px; font-size: 31px; font-weight: 500; letter-spacing: 0.5px; line-height: 1; }
  .contact-title { top: 150px; font-size: 13px; font-weight: 600; letter-spacing: 4px; line-height: 1; }
  .contact-email { top: 193px; font-size: 26px; font-weight: 300; line-height: 1.2; }
  .contact-phones {
    top: 261px; font-size: 18px; font-weight: 600; line-height: 1;
    display: flex; justify-content: center; align-items: center; gap: 6px;
  }
  .contact-phones .phone-item { display: inline-flex; align-items: center; gap: 6px; }
  .contact-phones .phone-item + .phone-item { margin-left: 10px; }
  .contact-phones svg { display: block; }
  .contact-address { top: 303px; font-size: 17.5px; font-weight: 400; line-height: 25px; }
  .contact-web { top: 371px; font-size: 18px; font-weight: 400; line-height: 1; }
  .contact-web strong { font-weight: 600; }
</style>
</head>
<body>
<main class="canvas">
  <section class="card card--front" aria-label="Card front">
    <div class="front-square"></div>
    <p class="front-name">R&amp;V ARCHITECTS</p>
    <p class="front-name-vertical">AND INTERIORS</p>
  </section>

  <section class="card card--back" aria-label="Card back">
    <div class="back-square"></div>
    <p class="back-name">R&amp;V ARCHITECTS</p>
    <p class="back-name-vertical">AND INTERIORS</p>

    <h1 class="contact contact-name">DANA WHITFIELD</h1>
    <p class="contact contact-title">PARTNER</p>
    <p class="contact contact-email">danaw@rvarchitects.com</p>
    <p class="contact contact-phones">
      <span class="phone-item">
        <svg width="12" height="13" viewBox="0 0 24 24" aria-hidden="true"><path fill="#111" d="M6.6 10.8a15.1 15.1 0 0 0 6.6 6.6l2.2-2.2a1 1 0 0 1 1-.25 11.4 11.4 0 0 0 3.6.57 1 1 0 0 1 1 1V20a1 1 0 0 1-1 1A17 17 0 0 1 3 4a1 1 0 0 1 1-1h3.5a1 1 0 0 1 1 1c0 1.25.2 2.46.57 3.6a1 1 0 0 1-.25 1z"/></svg>
        602 555 0148
      </span>
      <span class="phone-item">
        <svg width="9" height="15" viewBox="0 0 10 16" aria-hidden="true"><rect x="1" y="1" width="8" height="14" rx="1.3" fill="none" stroke="#111" stroke-width="1.6"/><rect x="4" y="12.3" width="2" height="1.2" fill="#111"/></svg>
        602 555 0193
      </span>
    </p>
    <p class="contact contact-address">2400 W. Meridian Ave., Suite 310<br>Phoenix, AZ 85007</p>
    <p class="contact contact-web"><strong>rvarchitects</strong>.com</p>
  </section>
</main>
</body>
</html>
```